Web Design Project

We need web design for a new baby products (nursery furniture) business in Australia.

The logo is already done, and I would like to reflect a similar theme throughout the website:
* Clean, white background.
* Use of lime green, purple and orange.
* Similar font to logo for headings
* FUNKY, FASHIONABLE, QUALITY feeling of website.

The main concept is to be attractive to discerning mums who are buying big items like a cot or chest of drawers. These are expensive items and will be considered the most important purchases for a newborn, so the website has to be enticing!!!
Updates

Hello,

Thank you for your submissions. I have received a few questions regarding the font and the coding of this website.

The job I am seeking is for design for an E-commerce store. The font was done by another pixel guild designer, so I do not know what type of font I am sorry.

I was hoping to have more designs by now, so please send them soon, this project is guaranteed!

I also ask you to read the brief properly please. The name of the business is Cradle Lane, as the logo says. The use of design that I have mentioned has only been demonstrated in a couple of designs submitted to me.

I look forward to seeing your work soon!

Kind Regards
Marla

Target Market(s)

Young mothers aged 25-45

Industry/Entity Type

Business

Requirements
Must have
• Must be funky, bright, energetic, attractive visually.
Nice to have
• I like the idea of some floral / design work in faded lime green, purple on some of the edges of different pages. Maybe islamic design? But has to be very fashionable.
Should not have
• Should not have any traditional ideas of baby websites.

ie- no stork, nappy images, teddybears etc.

```html
<!DOCTYPE html>
<html lang="en">
<head>
<meta charset="utf-8">
<title>Cradle Lane</title>
<link href="https://fonts.googleapis.com/css2?family=Arimo:wght@400;700&family=Ubuntu:wght@500;700&display=swap" rel="stylesheet">
<style>
:root{
  --bg:#f1fbdc;
  --bg-soft:#e6f7c4;
  --lime:#8ccc00;
  --purple:#cf52e6;
  --purple-deep:#a12ec0;
  --violet:#9a06cc;
  --orange:#ffab00;
  --orange-deep:#ff8f00;
  --gold:#ffc600;
  --gold-dark:#d9a300;
  --text:#2a2a2a;
  --muted:#6b6b6b;
  --white:#ffffff;
}
*{margin:0;padding:0;box-sizing:border-box}
html,body{width:1054px;height:1200px;overflow:hidden}
body{position:relative;font-family:"Arimo",Arial,sans-serif;color:var(--text);
  background:radial-gradient(ellipse 900px 700px at 50% 40%,var(--bg) 0%,var(--bg-soft) 100%)}
.page-texture{left:0;top:0;width:1054px;height:1200px;background:linear-gradient(180deg,rgba(255,255,255,.25),rgba(230,247,196,.4))}
.abs{position:absolute}
.top-stripe{left:0;top:0;width:1054px;height:5px;background:linear-gradient(var(--gold) 0 40%,var(--purple) 40% 100%)}

.brand{left:110px;top:32px;display:flex;align-items:center;gap:10px}
.brand-dot{width:60px;height:60px;border-radius:50%;background:var(--lime)}
.brand-name{font-weight:700;font-size:40px;color:var(--purple);line-height:1}

.account-link{top:60px;height:44px;color:var(--white);font-size:11px;text-align:center;padding-top:6px}
.account-link svg{display:block;margin:4px auto 0}
.account-link.orange{background:var(--orange)}
.account-link.purple{background:var(--purple)}
.account-link.deep{background:var(--orange-deep)}
.account-link.lime{background:var(--lime)}
.account-link.violet{background:var(--violet)}

.main-nav{left:110px;top:125px;width:835px;height:41px;background:var(--purple);border-bottom:4px solid var(--violet);display:flex;align-items:center;padding-left:25px;gap:31px;font-family:"Ubuntu",sans-serif;font-weight:700;font-size:13.5px;color:var(--white)}
.main-nav .active{color:var(--gold);position:relative}
.main-nav .active::after{content:"";position:absolute;left:50%;bottom:-13px;margin-left:-5px;border:5px solid transparent;border-bottom-color:var(--violet)}
.search-box{left:709px;top:130px;width:224px;height:26px;background:var(--white);border:2px solid #e6e6e6}
.search-box svg{position:absolute;left:4px;top:3px}
.search-tag{position:absolute;right:2px;top:3px;height:18px;padding:0 6px 0 10px;background:var(--purple);color:var(--white);font-size:11px;line-height:19px;clip-path:polygon(8px 0,100% 0,100% 100%,8px 100%,0 50%)}

.hero{left:108px;top:191px;width:837px;height:297px;background:var(--lime)}
.hero-title{left:36px;top:48px;font-size:24px;font-weight:400;color:var(--gold)}
.hero-text{left:36px;top:93px;width:250px;font-size:13px;line-height:16.4px;color:var(--white);letter-spacing:.3px}
.learn-more{left:35px;top:224px;width:99px;height:24px;background:var(--purple);color:var(--white);font-size:12px;line-height:24px;padding-left:10px}
.learn-more svg{position:absolute;right:8px;top:7px}
.hero-photo{left:316px;top:8px;width:511px;height:281px;background:linear-gradient(180deg,#d9c8a4 0%,#c7ab82 55%,#b8a38a 100%)}
.slider-dots{left:662px;top:269px;display:flex;gap:4px}
.slider-dots span{width:10px;height:10px;border-radius:50%;background:var(--gold);border:1px solid #a07a00}
.slider-dots span.on{background:#777}

.section-bar{left:108px;top:513px;width:837px;height:40px;background:var(--purple);color:var(--white);font-size:17px;line-height:40px;padding-left:25px}

.product-card{top:578px;width:254px;height:316px;background:var(--white);box-shadow:0 0 3px rgba(0,0,0,.25)}
.product-shot{left:12px;top:12px;width:230px;height:200px}
.product-info{left:4px;top:212px;width:246px;height:92px;background:#f3f3f3}
.product-name{left:12px;top:8px;font-size:15px;color:var(--lime)}
.product-price{left:10px;top:30px;font-size:25px;color:var(--lime)}
.add-cart{left:132px;top:34px;width:100px;height:21px;background:var(--lime);color:var(--white);font-size:12.5px;line-height:21px;text-align:center}
.product-actions{left:12px;top:67px;width:222px;display:flex;justify-content:space-between;font-size:12px;color:var(--muted)}
.carousel-arrow{top:694px;width:29px;height:84px;background:var(--gold);z-index:2}
.carousel-arrow::before{content:"";position:absolute;width:0;height:0;border:5px solid transparent}
.carousel-arrow.left::before{left:0;bottom:-10px;border-top-color:var(--gold-dark);border-right-color:var(--gold-dark)}
.carousel-arrow.right::before{right:0;top:-10px;border-bottom-color:var(--gold-dark);border-left-color:var(--gold-dark)}
.carousel-arrow svg{position:absolute;left:7px;top:28px}

.info-box{top:928px;width:253px;height:155px;background:var(--white);box-shadow:0 0 3px rgba(0,0,0,.25)}
.info-head{left:-6px;top:9px;width:253px;height:32px;background:linear-gradient(var(--purple),var(--purple-deep));color:var(--white);font-size:16.5px;font-weight:400;line-height:32px;padding-left:21px}
.info-body{left:15px;top:52px;width:228px;font-size:10.2px;line-height:16.4px}
.info-body .lead{color:var(--purple)}
.more-link{font-size:11px;color:var(--lime);text-decoration:underline}
.email-field{left:15px;top:58px;width:225px;height:28px;border:1px solid #bbb;font-size:10px;color:#888;padding:13px 0 0 6px}
.go-btn{position:absolute;right:-1px;top:-1px;width:35px;height:28px;background:var(--gold);color:var(--white);font-weight:700;font-size:13px;text-align:center;line-height:28px}
.small-label{font-size:12px;color:var(--purple)}
.pay-chip{width:22px;height:14px;border:1px solid #999}
.social-chip{width:17px;height:17px;background:#555}

.footer-rule{top:1118px;height:1px;background:#c8a6d4}
.footer-ornament{left:440px;top:1104px}
.footer-links{left:0;top:1150px;width:1054px;text-align:center;font-size:11px;color:#555}
.copyright{left:0;top:1172px;width:1054px;text-align:center;font-size:11px;color:#555}
.copyright b{color:var(--purple);font-weight:700}
</style>
</head>
<body>
<div class="abs page-texture"></div>
<div class="abs top-stripe"></div>

<div class="abs brand"><span class="brand-dot"></span><span class="brand-name">Cradle Lane</span></div>

<div class="abs account-link orange" style="left:470px;width:102px">My account
  <svg width="14" height="16" viewBox="0 0 14 16"><circle cx="7" cy="4.5" r="4" fill="#fff"/><path d="M0 16c0-5 3-7 7-7s7 2 7 7z" fill="#fff"/></svg></div>
<div class="abs account-link purple" style="left:576px;width:102px">My Wishlist
  <svg width="14" height="13" viewBox="0 0 14 13"><path d="M7 13L1 6.5A3.4 3.4 0 0 1 7 2a3.4 3.4 0 0 1 6 4.5z" fill="#fff"/></svg></div>
<div class="abs account-link deep" style="left:682px;width:83px">My Cart
  <svg width="18" height="15" viewBox="0 0 18 15"><path d="M1 1h3l2 8h9l2-6H5" fill="none" stroke="#fff" stroke-width="2"/><circle cx="7" cy="13" r="1.6" fill="#fff"/><circle cx="14" cy="13" r="1.6" fill="#fff"/></svg></div>
<div class="abs account-link lime" style="left:769px;width:94px">Check out
  <svg width="18" height="15" viewBox="0 0 18 15"><path d="M1 1h3l2 8h9l2-6H5" fill="none" stroke="#fff" stroke-width="2"/><circle cx="7" cy="13" r="1.6" fill="#fff"/><circle cx="14" cy="13" r="1.6" fill="#fff"/></svg></div>
<div class="abs account-link violet" style="left:868px;width:77px">Log In
  <svg width="12" height="14" viewBox="0 0 12 14"><path d="M3 6V4a3 3 0 0 1 6 0v2" fill="none" stroke="#fff" stroke-width="2"/><rect x="1" y="6" width="10" height="8" rx="1" fill="#fff"/></svg></div>

<nav class="abs main-nav">
  <span class="active">Home</span><span>About Us</span><span>Product Gallery</span><span>News</span><span>Testimonials</span><span>Contact Us</span>
</nav>
<div class="abs search-box">
  <svg width="18" height="18" viewBox="0 0 18 18"><circle cx="7" cy="7" r="5" fill="none" stroke="#b43ad6" stroke-width="2.5"/><path d="M11 11l6 6" stroke="#b43ad6" stroke-width="3"/></svg>
  <span class="search-tag">Search...</span>
</div>

<section class="abs hero">
  <h1 class="abs hero-title">Welcome To Our Site !</h1>
  <p class="abs hero-text">Sed eu nulla et justo elementum varius. Nulla commodo vehicula risus sed bibendum. Nullam eu blandit nulla. Proin ligula ante, scelerisque in accumsan id, condimentum ut justo. Vestibulum posuere tellus vel ante ultricies vel dictum enim feugiat.</p>
  <span class="abs learn-more">Learn More
    <svg width="14" height="10" viewBox="0 0 14 10"><path d="M0 5h12M8 1l4 4-4 4" fill="none" stroke="#fff" stroke-width="2"/></svg></span>
  <div class="abs hero-photo" role="img" aria-label="Bright nursery room with a wooden cot, dresser and window"></div>
  <div class="abs slider-dots"><span></span><span></span><span class="on"></span><span></span></div>
</section>

<div class="abs section-bar">Product Gallery</div>

<article class="abs product-card" style="left:119px">
  <div class="abs product-shot" role="img" aria-label="Dark wooden baby cot with pink bedding" style="background:linear-gradient(#3a2a30,#1e1a1c);opacity:.85"></div>
  <div class="abs product-info">
    <span class="abs product-name">Name Of Product</span>
    <span class="abs product-price">$ 3.50</span>
    <span class="abs add-cart">ADD TO CART</span>
    <div class="abs product-actions"><span>+ Add to Wishlist</span><span>+ Add Compare</span></div>
  </div>
</article>
<article class="abs product-card" style="left:403px">
  <div class="abs product-shot" role="img" aria-label="Cream wardrobe with a painted safari motif" style="background:linear-gradient(#efe6cc,#e2d6b2);left:72px;width:110px"></div>
  <div class="abs product-info">
    <span class="abs product-name">Name Of Product</span>
    <span class="abs product-price">$ 3.50</span>
    <span class="abs add-cart">ADD TO CART</span>
    <div class="abs product-actions"><span>+ Add to Wishlist</span><span>+ Add Compare</span></div>
  </div>
</article>
<article class="abs product-card" style="left:682px">
  <div class="abs product-shot" role="img" aria-label="Lime green baby bouncer on a black curved base" style="background:linear-gradient(160deg,#a6c23a 0%,#7c9a1c 55%,#1e1e1e 100%);opacity:.9"></div>
  <div class="abs product-info">
    <span class="abs product-name">Name Of Product</span>
    <span class="abs product-price">$ 3.50</span>
    <span class="abs add-cart">ADD TO CART</span>
    <div class="abs product-actions"><span>+ Add to Wishlist</span><span>+ Add Compare</span></div>
  </div>
</article>

<div class="abs carousel-arrow left" style="left:109px"><svg width="14" height="28" viewBox="0 0 14 28"><path d="M12 2L2 14l10 12" fill="none" stroke="#fff" stroke-width="2"/></svg></div>
<div class="abs carousel-arrow right" style="left:917px"><svg width="14" height="28" viewBox="0 0 14 28"><path d="M2 2l10 12L2 26" fill="none" stroke="#fff" stroke-width="2"/></svg></div>

<section class="abs info-box" style="left:116px">
  <h2 class="abs info-head">Aout Us</h2>
  <p class="abs info-body"><span class="lead">Lorem ipsum dolor sit amet, consectetur adipiscing elit.</span><br>Ut venenatis aliquet nisl, sit amet pretium magna venenatis a. Ut libero neque, pretium tincidunt ullamcorper vestibulum, vulputate ac nunc. Nam urna dui,<span class="more-link" style="float:right">Read More</span></p>
</section>
<section class="abs info-box" style="left:404px">
  <h2 class="abs info-head">Our Testimonial</h2>
  <p class="abs info-body" style="top:56px">Lorem ipsum dolor sit amet, consectetur adipiscing elit. Ut venenatis aliquet nisl, sit amet pretium magna venenatis a. Ut libero neque, pretium tincidunt ullamcorper vestibulum, vulputate ac nunc. Nam urna dui.<br><span class="more-link" style="float:right;font-size:12px">View All</span></p>
</section>
<section class="abs info-box" style="left:692px">
  <h2 class="abs info-head">Newsletter</h2>
  <div class="abs email-field">Enter the email...<span class="go-btn">Go</span></div>
  <span class="abs small-label" style="left:14px;top:103px">Payment Methods</span>
  <div class="abs" style="left:14px;top:128px;display:flex;gap:4px"><span class="pay-chip"></span><span class="pay-chip"></span><span class="pay-chip"></span><span class="pay-chip"></span></div>
  <span class="abs" style="left:138px;top:100px;width:1px;height:40px;background:var(--purple)"></span>
  <span class="abs small-label" style="left:166px;top:103px">Follow Us</span>
  <div class="abs" style="left:166px;top:125px;display:flex;gap:4px"><span class="social-chip"></span><span class="social-chip"></span><span class="social-chip"></span><span class="social-chip"></span></div>
</section>

<div class="abs footer-rule" style="left:116px;width:300px"></div>
<div class="abs footer-rule" style="left:640px;width:305px"></div>
<svg class="abs footer-ornament" width="174" height="30" viewBox="0 0 174 30"><path d="M0 15h174" stroke="#c8a6d4"/><circle cx="87" cy="15" r="4" fill="#d27ee6"/></svg>
<div class="abs footer-links">Site Map | Search Terms | Advanced Search | Order and Returns | Contact Us | About Us \ Customer Service | Privacy Policy</div>
<div class="abs copyright">Copyright © 2012 <b>Cradle Lane</b>&nbsp; All rights reserved.</div>
</body>
</html>
```